We are an appraisal and dispute resolution company that works with insurance companies and insureds.

We need a website built that appeals to insurance companies as well as insureds to entrust we can assist come to a resolution with their property insurance claim.

Target Market(s)

Insurance Carriers and Insureds

Industry/Entity Type

Insurance

Coding

Coded - Design and coding required

Number of Pages Required

5+ page

Requirements
Must have
• Would like to click on pages and it take you down one page to that specific section
Nice to have
• Clean look

```html
<!DOCTYPE html>
<html lang="en">
<head>
<meta charset="utf-8">
<title>Claimwell Appraisal and Resolution</title>
<link href="https://fonts.googleapis.com/css2?family=Lato:ital,wght@0,400;0,700;0,900;1,700&family=Montserrat:wght@400;500;600&display=swap" rel="stylesheet">
<style>
:root{
  --teal:#3cc4c9;
  --teal-dark:#2eb3b8;
  --navy:#2f3443;
  --navy-deep:#22252d;
  --ink:#1f2330;
  --muted:#7b7f88;
  --white:#ffffff;
  --line:rgba(255,255,255,.75);
}
*{box-sizing:border-box;margin:0;padding:0}
html,body{width:1200px;height:4630px;overflow:hidden}
body{font-family:'Lato',sans-serif;color:var(--ink);background:var(--white);position:relative}
section,header,footer{position:relative;width:1200px;overflow:hidden}
.abs{position:absolute}
a{color:inherit;text-decoration:none}

/* hero */
.hero{height:606px;background:linear-gradient(100deg,#5a3a2c 0%,#7d5242 35%,#9a7a66 60%,#6d6458 100%)}
.hero-photo{position:absolute;inset:0}
.hero-shade{position:absolute;inset:0;background:linear-gradient(90deg,rgba(20,18,20,.55),rgba(20,18,20,.15) 60%,rgba(0,0,0,0))}
.brand{position:absolute;left:111px;top:14px;color:var(--white)}
.brand-name{font-weight:900;font-size:46px;letter-spacing:1px;line-height:46px}
.brand-sub{font-size:8px;font-weight:700;letter-spacing:.3px;margin-top:4px}
.topbar{position:absolute;right:113px;top:14px;display:flex;align-items:center;gap:8px;color:var(--white);font-size:15px}
.topbar .phone{margin-right:16px;display:flex;align-items:center;gap:6px}
.social-dot{width:24px;height:24px;border:1.5px solid var(--white);border-radius:50%}
.nav{position:absolute;right:113px;top:52px;display:flex;gap:40px;color:var(--white);font-size:16px;font-weight:700}
.nav a.active{border-bottom:2px solid var(--white);padding-bottom:4px}
.hero-title{position:absolute;left:150px;top:185px;font-size:98px;font-weight:700;color:var(--white);letter-spacing:2px}
.hero-text{position:absolute;left:153px;top:296px;width:455px;font-size:16px;line-height:26px;color:var(--white);font-weight:700}
.btn{display:inline-flex;align-items:center;justify-content:center;background:var(--teal);color:var(--white);font-weight:700;font-size:16px;border-radius:30px;text-transform:uppercase}
.hero .btn{position:absolute;left:149px;top:395px;width:183px;height:51px}
.arrow-circle{position:absolute;width:38px;height:38px;border:1.5px solid var(--white);border-radius:50%;display:flex;align-items:center;justify-content:center}
.slider-lines{position:absolute;left:515px;top:558px;display:flex;gap:6px}
.slider-lines span{width:36px;height:3px;background:rgba(255,255,255,.5)}
.slider-lines span:first-child{background:var(--white)}

/* welcome */
.welcome{height:544px}
.welcome-frame{position:absolute;left:111px;top:97px;width:458px;height:350px;background:var(--teal)}
.welcome-photo{position:absolute;left:119px;top:106px;width:458px;height:350px;background:linear-gradient(120deg,#e9ebee,#c9ced6 55%,#5d6c85)}
.welcome h2{position:absolute;left:622px;top:96px;font-size:30px;font-weight:900;color:var(--ink)}
.welcome h3{position:absolute;left:622px;top:138px;font-size:18px;font-weight:700;color:var(--ink)}
.welcome p{position:absolute;left:622px;top:180px;width:467px;font-size:14px;line-height:26.5px;color:var(--muted);text-align:justify}
.welcome .btn{position:absolute;left:625px;top:418px;width:180px;height:45px;font-size:15px}

/* solutions */
.solutions{height:841px;background:var(--navy)}
.solutions-bg{position:absolute;inset:0;background:linear-gradient(90deg,rgba(255,255,255,0) 50%,rgba(255,255,255,.05))}
.solutions h2{position:absolute;left:110px;top:152px;font-size:34px;font-weight:900;color:var(--white)}
.solutions .intro{position:absolute;left:110px;top:208px;width:300px;font-size:14px;line-height:28px;color:var(--white)}
.card{position:absolute;width:309px;height:324px;border:1.5px solid var(--line);border-radius:4px;color:var(--white);text-align:center}
.card svg{margin-top:22px}
.card h4{font-size:20px;font-weight:700;margin-top:14px}
.card p{font-size:12.5px;line-height:25.5px;margin:10px 22px 0}
.card a{display:inline-block;margin-top:14px;font-size:14.5px;font-weight:700;text-decoration:underline}

/* people */
.people{height:516px}
.section-title{position:absolute;left:0;width:100%;text-align:center;font-size:34px;font-weight:900;color:var(--ink)}
.person{position:absolute;top:155px;width:233px;height:273px}
.person-photo{height:231px;background:linear-gradient(160deg,#d7dbe0,#8e98a6 60%,#2f3b52)}
.person-name{position:absolute;left:0;top:166px;width:100%;height:65px;background:rgba(40,44,56,.55);color:var(--white);text-align:center;padding-top:8px}
.person-name strong{display:block;font-size:20px}
.person-name span{font-size:14px}
.person .more{height:42px;background:var(--teal);color:var(--white);font-weight:700;font-size:16px;display:flex;align-items:center;justify-content:center;gap:6px}

/* reviews */
.reviews{height:533px;background:linear-gradient(180deg,#47c9cd,#3dbfc4)}
.reviews h2{position:absolute;left:0;width:100%;text-align:center;top:80px;font-size:36px;font-weight:900;color:var(--white)}
.reviews .sub{position:absolute;left:0;width:100%;text-align:center;top:134px;font-size:13px;font-weight:700;font-style:italic;color:var(--white)}
.review{position:absolute;top:224px;width:460px;height:198px;background:var(--white);font-family:'Montserrat',sans-serif;padding:46px 14px 0 14px}
.review .avatar{position:absolute;left:14px;top:-43px;width:82px;height:82px;border-radius:50%;border:3px solid var(--teal-dark);background:linear-gradient(160deg,#dfe3e8,#7a8596)}
.review p{font-size:15px;line-height:28px;color:#6c7079}
.review strong{display:block;font-size:16px;font-weight:600;color:var(--ink);margin-top:4px}
.review small{font-size:14px;color:#6c7079}
.review .quote{position:absolute;right:26px;top:124px;font-family:'Lato',sans-serif;font-size:80px;font-weight:900;color:var(--teal);line-height:80px}
.dots{position:absolute;left:550px;top:2951px}

/* news */
.news{height:728px}
.news-photo{position:absolute;background:linear-gradient(135deg,#c9b7a3,#8c7663 60%,#4f5b70)}
.news-date{position:absolute;font-size:14px;color:var(--ink);display:flex;align-items:center;gap:5px}
.news-title{position:absolute;font-weight:900;color:var(--ink)}
.news-text{position:absolute;font-size:12.5px;line-height:27px;color:var(--muted)}

/* contact */
.contact{height:522px;background:var(--navy)}
.contact .eyebrow{position:absolute;left:109px;top:176px;font-size:20px;color:var(--white)}
.contact h2{position:absolute;left:109px;top:230px;font-size:38px;line-height:46px;font-weight:700;color:var(--white);width:340px}
.field{position:absolute;background:var(--white);border:1px solid #d8dbe0;font-size:13px;color:#8a8e96;padding:0 10px;display:flex;align-items:center;justify-content:space-between}
.field.area{align-items:flex-start;padding-top:14px}
.send{position:absolute;left:491px;top:385px;width:266px;height:50px;border:1.5px solid var(--white);color:var(--white);font-weight:700;font-size:16px;display:flex;align-items:center;justify-content:center}

/* footer */
.footer{height:340px;background:var(--navy-deep);color:var(--white)}
.footer h5{position:absolute;top:78px;font-size:17px;font-weight:700}
.footer ul{position:absolute;list-style:none;font-size:14px;line-height:26px}
.footer .info{position:absolute;font-size:14px;line-height:23px;display:flex;gap:10px}
.footer .subscribe{position:absolute;left:862px;top:112px;width:215px;font-size:13px;line-height:22px}
.footer .mail{position:absolute;left:862px;top:163px;width:226px;height:44px;background:var(--white);color:#666;font-size:13px;padding-left:16px;display:flex;align-items:center}
.footer .mail span.go{position:absolute;right:0;top:0;width:44px;height:44px;background:var(--teal);display:flex;align-items:center;justify-content:center}
.footer .rule{position:absolute;left:110px;top:275px;width:979px;height:1px;background:rgba(255,255,255,.4)}
.footer .copy{position:absolute;left:110px;top:302px;font-size:13px}
.footer .legal{position:absolute;right:112px;top:302px;font-size:13px}
.foot-social{position:absolute;left:112px;top:168px;display:flex;gap:8px}
.foot-social span{width:31px;height:31px;border-radius:50%;background:var(--white)}
</style>
</head>
<body>

<header class="hero" id="home">
  <div class="hero-photo" role="img" aria-label="Smiling family of three standing in front of their brick house"></div>
  <div class="hero-shade"></div>
  <div class="brand">
    <div class="brand-name">CLAIMWELL</div>
    <div class="brand-sub">CLAIMWELL APPRAISAL AND RESOLUTION</div>
  </div>
  <div class="topbar">
    <span class="phone">
      <svg width="14" height="14" viewBox="0 0 24 24" fill="#fff"><path d="M6.6 10.8a15 15 0 006.6 6.6l2.2-2.2c.3-.3.7-.4 1-.2 1.1.4 2.3.6 3.6.6.6 0 1 .4 1 1V20c0 .6-.4 1-1 1A17 17 0 013 4c0-.6.4-1 1-1h3.5c.6 0 1 .4 1 1 0 1.3.2 2.5.6 3.6.1.3 0 .7-.2 1z"/></svg>
      Phone: (+1) 555 014 2020
    </span>
    <span class="social-dot"></span><span class="social-dot"></span><span class="social-dot"></span><span class="social-dot"></span>
  </div>
  <nav class="nav">
    <a href="#home" class="active">Home</a>
    <a href="#about">About Us</a>
    <a href="#solutions">Our Solutions</a>
    <a href="#team">Our Team</a>
    <a href="#news">Resources</a>
    <a href="#contact">Contact Us</a>
  </nav>
  <h1 class="hero-title">CLAIMWELL</h1>
  <p class="hero-text">Lorem ipsum dolor sit amet, consectetur adipiscing elit, sed do eiusmod tempor incididunt ut labore et dolore magna aliqua. Ut enim ad minim veniam,</p>
  <a class="btn" href="#contact">Get Started</a>
  <span class="arrow-circle" style="left:46px;top:304px"><svg width="12" height="18" viewBox="0 0 12 18"><path d="M10 1L2 9l8 8" stroke="#fff" stroke-width="1.6" fill="none"/></svg></span>
  <span class="arrow-circle" style="left:1110px;top:304px"><svg width="12" height="18" viewBox="0 0 12 18"><path d="M2 1l8 8-8 8" stroke="#fff" stroke-width="1.6" fill="none"/></svg></span>
  <div class="slider-lines"><span></span><span></span><span></span></div>
</header>

<section class="welcome" id="about">
  <div class="welcome-frame"></div>
  <div class="welcome-photo" role="img" aria-label="Advisor in a suit handing a document to a client across a desk"></div>
  <h2>WELCOME TO</h2>
  <h3>CLAIMWELL APPRAISAL AND RESOLUTION</h3>
  <p>Marcus Hollander is the Financial Strategist and Founder who partners with C-Suite Executives, Family Offices, Real Estate Investors and Closely Held Business Owners to protect and maximize their wealth. After spending 15 years in the commercial banking and wealth management as a commercial and private lender Marcus developed a comprehensive approach to asset protection and wealth preservation. The comprehensive approach creates a plan that focuses on the client's income tax first with wealth preservation</p>
  <a class="btn" href="#solutions">Learn More</a>
</section>

<section class="solutions" id="solutions">
  <div class="solutions-bg" role="img" aria-label="Faint photograph of a modern building behind the dark overlay"></div>
  <h2>OUR SOLUTIONS</h2>
  <p class="intro">Lorem ipsum dolor sit amet, conr adipiscing elit, sed do eiusmod tempor incidt ut labore et dolore maga aliqua. is ipsum suspendisse ultrices gravida. comodo viverra maecenas accumsan lacus vel facilisis.</p>

  <div class="card" style="left:446px;top:86px">
    <svg width="62" height="64" viewBox="0 0 62 64" fill="none" stroke="#fff" stroke-width="2"><rect x="8" y="4" width="36" height="48" rx="2"/><path d="M16 16h20M16 24h20M16 32h14"/><circle cx="44" cy="46" r="9"/><path d="M40 54l-2 8 6-3 6 3-2-8"/></svg>
    <h4>The standard Lorem Ipsum</h4>
    <p>Lorem ipsum dolor sit onsectetur adipiscing elit, sed eiusmod temr incididunt ut labore et dolore magna aliqua. Ut enim ad minim veniam, quis nostrud exercitation</p>
    <a href="#solutions">READ MORE &gt;&gt;</a>
  </div>
  <div class="card" style="left:780px;top:86px">
    <svg width="62" height="64" viewBox="0 0 62 64" fill="none" stroke="#fff" stroke-width="2"><circle cx="22" cy="42" r="14"/><path d="M22 34v16M18 38h6a3 3 0 010 6h-4a3 3 0 000 6h6"/><path d="M40 50V20M40 28c-8 0-12-6-12-12 8 0 12 6 12 12zM40 24c0-8 6-12 14-12 0 8-6 12-14 12z"/><path d="M32 58h24"/></svg>
    <h4>The standard Lorem Ipsum</h4>
    <p>Lorem ipsum dolor sit onsectetur adipiscing elit, sed eiusmod temr incididunt ut labore et dolore magna aliqua. Ut enim ad minim veniam, quis nostrud exercitation</p>
    <a href="#solutions">READ MORE &gt;&gt;</a>
  </div>
  <div class="card" style="left:111px;top:431px">
    <svg width="62" height="64" viewBox="0 0 62 64" fill="none" stroke="#fff" stroke-width="2"><path d="M22 40V28M30 40V22M38 40V16M46 40V10"/><path d="M14 26l12-10 8 6 14-14"/><path d="M6 50c8-6 16-6 22-2h12c3 0 3 4 0 4H28M6 58c10-4 24 0 36-8l10-8"/></svg>
    <h4>The standard Lorem Ipsum</h4>
    <p>Lorem ipsum dolor sit onsectetur adipiscing elit, sed eiusmod temr incididunt ut labore et dolore magna aliqua. Ut enim ad minim veniam, quis nostrud exercitation</p>
    <a href="#solutions">READ MORE &gt;&gt;</a>
  </div>
  <div class="card" style="left:446px;top:431px">
    <svg width="62" height="64" viewBox="0 0 62 64" fill="none" stroke="#fff" stroke-width="2"><path d="M14 28c-4 6-4 20 6 24h12c10-4 10-18 6-24z"/><path d="M18 12h16l-4 14H22z"/><path d="M26 32v14M22 36h6a2 2 0 010 4h-4a2 2 0 000 4h6"/><rect x="40" y="36" width="16" height="18"/><path d="M42 36v-8h12v8M44 42h8M44 48h8"/></svg>
    <h4>The standard Lorem Ipsum</h4>
    <p>Lorem ipsum dolor sit onsectetur adipiscing elit, sed eiusmod temr incididunt ut labore et dolore magna aliqua. Ut enim ad minim veniam, quis nostrud exercitation</p>
    <a href="#solutions">READ MORE &gt;&gt;</a>
  </div>
  <div class="card" style="left:780px;top:431px">
    <svg width="62" height="64" viewBox="0 0 62 64" fill="none" stroke="#fff" stroke-width="2"><rect x="12" y="4" width="34" height="50"/><path d="M16 8v50h34V14"/><text x="18" y="20" fill="#fff" stroke="none" font-family="Lato, sans-serif" font-size="11" font-weight="700">TAX</text><path d="M18 24h22M22 44l10-12"/><circle cx="23" cy="34" r="2"/><circle cx="32" cy="43" r="2"/></svg>
    <h4>The standard Lorem Ipsum</h4>
    <p>Lorem ipsum dolor sit onsectetur adipiscing elit, sed eiusmod temr incididunt ut labore et dolore magna aliqua. Ut enim ad minim veniam, quis nostrud exercitation</p>
    <a href="#solutions">READ MORE &gt;&gt;</a>
  </div>
</section>

<section class="people" id="team">
  <h2 class="section-title" style="top:80px">MEET OUR PEOPLE</h2>
  <div class="person" style="left:110px">
    <div class="person-photo" role="img" aria-label="Portrait of a smiling man in a navy suit"></div>
    <div class="person-name"><strong>Owen Calder</strong><span>Lorem Ipsum</span></div>
    <a class="more" href="#team">LEARN MORE <svg width="16" height="10" viewBox="0 0 16 10"><path d="M0 5h13M10 1l4 4-4 4" stroke="#fff" stroke-width="2" fill="none"/></svg></a>
  </div>
  <div class="person" style="left:357px">
    <div class="person-photo" role="img" aria-label="Portrait of a man in a blazer outside a building"></div>
    <div class="person-name"><strong>Reid Lawton</strong><span>Lorem Ipsum</span></div>
    <a class="more" href="#team">LEARN MORE <svg width="16" height="10" viewBox="0 0 16 10"><path d="M0 5h13M10 1l4 4-4 4" stroke="#fff" stroke-width="2" fill="none"/></svg></a>
  </div>
  <div class="person" style="left:604px">
    <div class="person-photo" role="img" aria-label="Portrait of a man in a suit with a city skyline behind"></div>
    <div class="person-name"><strong>Grant Mercer</strong><span>Lorem Ipsum</span></div>
    <a class="more" href="#team">LEARN MORE <svg width="16" height="10" viewBox="0 0 16 10"><path d="M0 5h13M10 1l4 4-4 4" stroke="#fff" stroke-width="2" fill="none"/></svg></a>
  </div>
  <div class="person" style="left:852px">
    <div class="person-photo" role="img" aria-label="Portrait of a man in a suit in a bright office"></div>
    <div class="person-name"><strong>Dean Whitaker</strong><span>Lorem Ipsum</span></div>
    <a class="more" href="#team">LEARN MORE <svg width="16" height="10" viewBox="0 0 16 10"><path d="M0 5h13M10 1l4 4-4 4" stroke="#fff" stroke-width="2" fill="none"/></svg></a>
  </div>
</section>

<section class="reviews" id="reviews">
  <h2>CLIENT REVIEWS</h2>
  <p class="sub">Lorem ipsum dolor sit amet, consectetur adipiscing elit, sed do eiusmod tempor incididunt ut</p>
  <span class="arrow-circle" style="left:20px;top:304px"><svg width="20" height="16" viewBox="0 0 20 16"><path d="M18 8H3M8 2L2 8l6 6" stroke="#fff" stroke-width="1.8" fill="none"/></svg></span>
  <div class="review" style="left:92px">
    <span class="avatar" role="img" aria-label="Client portrait"></span>
    <p>Lorem ipsum dolor sit amet, consectetur adipiscing elit, sed do eiusmod tempor incididunt ut labore et dolore magna aliqua. Quis ipsum suspendisse</p>
    <strong>Evan Marsh</strong><small>Lorem ipsum dolor</small>
    <span class="quote">&ldquo;</span>
  </div>
  <div class="review" style="left:562px">
    <span class="avatar" role="img" aria-label="Client portrait"></span>
    <p>Lorem ipsum dolor sit amet, consectetur adipiscing elit, sed do eiusmod tempor incididunt ut labore et dolore magna aliqua. Quis ipsum suspendisse</p>
    <strong>Evan Marsh</strong><small>Lorem ipsum dolor</small>
    <span class="quote">&ldquo;</span>
  </div>
  <div class="review" style="left:1033px">
    <span class="avatar" role="img" aria-label="Client portrait"></span>
    <p>Lorem ipsum dolor sit amet, consectetur adipiscing elit, sed do eiusmod tempor incididunt ut labore et dolore magna aliqua. Quis ipsum suspendisse</p>
    <strong>Evan Marsh</strong><small>Lorem ipsum dolor</small>
  </div>
  <svg class="abs" style="left:548px;top:444px" width="68" height="14" viewBox="0 0 68 14"><circle cx="7" cy="7" r="6" fill="#fff"/><circle cx="25" cy="7" r="6" fill="#fff" opacity=".6"/><circle cx="43" cy="7" r="6" fill="#fff" opacity=".6"/><circle cx="61" cy="7" r="6" fill="#fff" opacity=".6"/></svg>
</section>

<section class="news" id="news">
  <h2 class="section-title" style="top:76px">LATEST NEWS</h2>
  <div class="news-photo" style="left:110px;top:150px;width:472px;height:291px;background:linear-gradient(135deg,#ecebe8,#d4c6b4 55%,#a08468)" role="img" aria-label="Family sitting among moving boxes under a drawn house outline"></div>
  <div class="news-date" style="left:110px;top:465px"><svg width="14" height="14" viewBox="0 0 14 14"><rect x="1" y="2" width="12" height="11" fill="#2f3443"/><rect x="3" y="6" width="8" height="5" fill="#fff"/></svg>15 April,2020</div>
  <div class="news-title" style="left:110px;top:500px;width:470px;font-size:18.5px;line-height:27px">Lorem ipsum dolor sit amet, consectetur adipiscing elit, sed do eiusmod tempor</div>
  <p class="news-text" style="left:110px;top:563px;width:472px">Lorem ipsum dolor sit amet, consectetur adipisicineiusmod tempordidunt ut labore et dolore magna aliqua. Quis ipsum pendisse ultrices gravida.Lorem ipsum dolor sit amet, consectetur adipisicineiusmod</p>

  <div class="news-photo" style="left:600px;top:150px;width:237px;height:143px;background:linear-gradient(135deg,#dfe3e8,#9aa4b2)" role="img" aria-label="Hands signing a contract on a desk"></div>
  <div class="news-date" style="left:600px;top:306px"><svg width="14" height="14" viewBox="0 0 14 14"><rect x="1" y="2" width="12" height="11" fill="#2f3443"/><rect x="3" y="6" width="8" height="5" fill="#fff"/></svg>15 April,2020</div>
  <div class="news-title" style="left:600px;top:336px;width:240px;font-size:14.5px;line-height:27px">Lorem ipsum dolorconsectetur adipiscing elit, sed do eiusmod</div>

  <div class="news-photo" style="left:852px;top:150px;width:237px;height:143px;background:linear-gradient(135deg,#b0856a,#5c4a44 60%,#34405a)" role="img" aria-label="Agent holding a small model house beside paperwork"></div>
  <div class="news-date" style="left:852px;top:306px"><svg width="14" height="14" viewBox="0 0 14 14"><rect x="1" y="2" width="12" height="11" fill="#2f3443"/><rect x="3" y="6" width="8" height="5" fill="#fff"/></svg>15 April,2020</div>
  <div class="news-title" style="left:852px;top:336px;width:240px;font-size:14.5px;line-height:27px">Lorem ipsum dolorconsectetur adipiscing elit, sed do eiusmod</div>

  <div class="news-photo" style="left:600px;top:409px;width:237px;height:143px;background:linear-gradient(135deg,#3a4458,#8a7a70 55%,#c9b19c)" role="img" aria-label="Handshake over a desk with a model house"></div>
  <div class="news-date" style="left:600px;top:567px"><svg width="14" height="14" viewBox="0 0 14 14"><rect x="1" y="2" width="12" height="11" fill="#2f3443"/><rect x="3" y="6" width="8" height="5" fill="#fff"/></svg>15 April,2020</div>
  <div class="news-title" style="left:600px;top:597px;width:240px;font-size:14.5px;line-height:27px">Lorem ipsum dolorconsectetur adipiscing elit, sed do eiusmod</div>

  <div class="news-photo" style="left:852px;top:409px;width:237px;height:143px;background:linear-gradient(135deg,#f2f2f2,#d49a62 55%,#8a5a34)" role="img" aria-label="Wooden house model shielded by a hand"></div>
  <div class="news-date" style="left:852px;top:567px"><svg width="14" height="14" viewBox="0 0 14 14"><rect x="1" y="2" width="12" height="11" fill="#2f3443"/><rect x="3" y="6" width="8" height="5" fill="#fff"/></svg>15 April,2020</div>
  <div class="news-title" style="left:852px;top:597px;width:240px;font-size:14.5px;line-height:27px">Lorem ipsum dolorconsectetur adipiscing elit, sed do eiusmod</div>
</section>

<section class="contact" id="contact">
  <p class="eyebrow">CONTACT US</p>
  <h2>Don&rsquo;t Hesitate to Contact us for any Information.</h2>
  <div class="field" style="left:491px;top:88px;width:294px;height:47px">First Name</div>
  <div class="field" style="left:792px;top:88px;width:297px;height:47px">Last Name</div>
  <div class="field" style="left:491px;top:149px;width:294px;height:47px">Email</div>
  <div class="field" style="left:792px;top:149px;width:297px;height:47px">Phone</div>
  <div class="field" style="left:491px;top:209px;width:294px;height:46px">Select Service <svg width="10" height="6" viewBox="0 0 10 6"><path d="M0 0h10L5 6z" fill="#333"/></svg></div>
  <div class="field" style="left:792px;top:209px;width:297px;height:46px">Select Industry <svg width="10" height="6" viewBox="0 0 10 6"><path d="M0 0h10L5 6z" fill="#333"/></svg></div>
  <div class="field area" style="left:491px;top:266px;width:598px;height:103px">How Can We Help You</div>
  <a class="send" href="#contact">SEND US YOUR ENQUIRY</a>
</section>

<footer class="footer">
  <div class="brand" style="top:74px">
    <div class="brand-name" style="font-size:42px">CLAIMWELL</div>
    <div class="brand-sub">CLAIMWELL APPRAISAL AND RESOLUTION</div>
  </div>
  <div class="foot-social"><span></span><span></span><span></span><span></span></div>

  <h5 style="left:421px">QUICK LINKS</h5>
  <ul style="left:421px;top:106px">
    <li><a href="#home">Home</a></li>
    <li><a href="#about">About Us</a></li>
    <li><a href="#solutions">Our Solutions</a></li>
    <li><a href="#team">Our team</a></li>
    <li><a href="#contact">Contact Us</a></li>
  </ul>

  <h5 style="left:584px">CONTACT INFO</h5>
  <div class="info" style="left:584px;top:108px">
    <svg width="14" height="18" viewBox="0 0 14 18" style="margin-top:3px"><path d="M7 1a6 6 0 016 6c0 4-6 10-6 10S1 11 1 7a6 6 0 016-6z" stroke="#fff" stroke-width="1.4" fill="none"/><circle cx="7" cy="7" r="2" fill="#fff"/></svg>
    <span>48 Harbor Lane, Fairview<br>10150, United States</span>
  </div>
  <div class="info" style="left:584px;top:168px">
    <svg width="16" height="16" viewBox="0 0 24 24" style="margin-top:3px"><path d="M6.6 10.8a15 15 0 006.6 6.6l2.2-2.2c.3-.3.7-.4 1-.2 1.1.4 2.3.6 3.6.6.6 0 1 .4 1 1V20c0 .6-.4 1-1 1A17 17 0 013 4c0-.6.4-1 1-1h3.5c.6 0 1 .4 1 1 0 1.3.2 2.5.6 3.6.1.3 0 .7-.2 1z" stroke="#fff" stroke-width="1.6" fill="none"/></svg>
    <span>555 014 2020</span>
  </div>
  <div class="info" style="left:584px;top:207px">
    <svg width="16" height="12" viewBox="0 0 16 12" style="margin-top:6px"><rect x="1" y="1" width="14" height="10" stroke="#fff" stroke-width="1.3" fill="none"/><path d="M1 1l7 6 7-6" stroke="#fff" stroke-width="1.3" fill="none"/></svg>
    <span>info@claimwell.example</span>
  </div>

  <h5 style="left:861px">SUBSCRIBE NEWSLETTER</h5>
  <p class="subscribe">Lorem ips sit amet, consectetur adipiscing elit, sed do</p>
  <div class="mail">email address
    <span class="go"><svg width="18" height="18" viewBox="0 0 18 18"><path d="M1 8L17 1l-5 16-3-6z" stroke="#fff" stroke-width="1.5" fill="none"/><path d="M9 11l8-10" stroke="#fff" stroke-width="1.5"/></svg></span>
  </div>

  <div class="rule"></div>
  <p class="copy">Copyright &copy; 2021 CLAIMWELL.All Rights Reserved.</p>
  <p class="legal">Terms &amp;Conditions &nbsp;&nbsp;|&nbsp;&nbsp; Privacy Policy</p>
</footer>

</body>
</html>
```